High end business card design for custom homebuilding company

Looking for a high end business card design that is unique and elegant. Can use embossing, foil printing, laser die cutting, or any high end printing technique or high end paper. Will upload current design so you can see the logo and what we are using currently, but we want something more unique and elegant. I included our logo to help with design.

Target Market(s)

High end custom home buyers of $1.5 million plus homes. Also real estate developers of high end communities.

Industry/Entity Type

Business

Contact Information for Business Card

Double sided. We want something very elegant and expensive looking. We are looking to incorporate a combination of perhaps linen paper or a high end paper, with foil stamping or embossing/debossing to make the card look unique, but still elegant. We tend to use blacks and golds, but are open to any ideas. Looking for creative and unique design.

Colors

Designer to choose colors to be used in the design.

Requirements
Must have
• High end, elegant look. Can use foil, embossing, or high end papers like linen. We want to make the card unique and interesting, but elegant and expensive looking.
Nice to have
• I am including just some cards I saw that looked interesting for one reason or another. I like a clean elegant design and like both the clean white style, and the blacks. So not sure if we want a black design or white. Would like to see both.

```html
<!DOCTYPE html>
<html lang="en">
<head>
<meta charset="utf-8">
<title>Hollowbrook Custom Homes – Business Card</title>
<link href="https://fonts.googleapis.com/css2?family=Cinzel:wght@400;600&family=Source+Sans+3:wght@400;600&display=swap" rel="stylesheet">
<style>
  :root {
    --backdrop: #3b312d;
    --paper: #fbfbfa;
    --paper-shade: #efefed;
    --ink: #1e1e1e;
    --ink-soft: #4a4a4a;
    --gold: #c2a52c;
    --rule: #6d6d6d;
    --social: #2f6fb3;
    --social-alt: #d23a32;
  }
  * { box-sizing: border-box; margin: 0; padding: 0; }
  html, body {
    width: 1200px; height: 844px; overflow: hidden;
    background: var(--backdrop);
  }
  .canvas {
    position: relative; width: 1200px; height: 844px;
    display: flex; align-items: center; justify-content: center; gap: 50px;
  }
  .card {
    position: relative; width: 540px; height: 309px;
    background: var(--paper);
    box-shadow: 0 6px 18px rgba(0,0,0,.35);
    overflow: hidden;
  }

  /* Front */
  .card-front { padding: 26px 34px 0 34px; font-family: "Source Sans 3", sans-serif; color: var(--ink-soft); }
  .brand {
    position: absolute; top: 30px; right: 40px;
    display: flex; align-items: center; gap: 10px;
  }
  .brand-mark { width: 22px; height: 22px; border-radius: 50%; background: var(--ink); }
  .brand-name {
    font-family: "Cinzel", serif; font-weight: 600; font-size: 26px;
    color: var(--ink); letter-spacing: 1px; line-height: 1;
  }
  .brand-name small { display: block; font-size: 9px; letter-spacing: 4.4px; margin-top: 3px; text-align: right; }
  .rule { position: absolute; left: 34px; right: 34px; height: 1px; background: var(--rule); }
  .rule-1 { top: 92px; left: 260px; }
  .rule-2 { top: 118px; left: 180px; }
  .rule-3 { top: 178px; }
  .person { position: absolute; top: 132px; left: 34px; }
  .person-name { font-family: "Cinzel", serif; font-size: 19px; color: var(--ink); letter-spacing: .5px; line-height: 1; }
  .person-name .first { color: var(--gold); }
  .person-role { font-size: 13px; margin-top: 3px; }
  .address { position: absolute; top: 188px; left: 34px; font-size: 13px; }
  .contact { position: absolute; top: 216px; left: 34px; font-size: 13px; line-height: 1.5; }
  .contact .label { color: var(--gold); }
  .contact .web { color: var(--gold); margin-left: 8px; }
  .follow {
    position: absolute; bottom: 18px; left: 34px;
    display: flex; align-items: center; gap: 5px;
    font-size: 12px; font-weight: 600; color: var(--ink); letter-spacing: .3px;
  }
  .follow-label { margin-right: 5px; }
  .social-dot { width: 17px; height: 17px; border-radius: 50%; background: var(--social); }
  .social-dot.alt { background: var(--social-alt); }

  /* Back */
  .card-back { display: flex; align-items: center; justify-content: center; }
  .emboss-field {
    position: absolute; inset: 0;
    background: linear-gradient(135deg, var(--paper) 0%, var(--paper-shade) 50%, var(--paper) 100%);
  }
  .back-brand {
    position: relative; display: flex; align-items: center; gap: 8px;
    font-family: "Cinzel", serif; font-weight: 600; font-size: 16px; color: var(--ink); letter-spacing: 1px;
  }
  .back-brand .brand-mark { width: 14px; height: 14px; }
</style>
</head>
<body>
<main class="canvas">
  <section class="card card-front" aria-label="Business card front">
    <div class="brand">
      <span class="brand-mark"></span>
      <div class="brand-name">Hollowbrook<small>CUSTOM HOMES</small></div>
    </div>
    <div class="rule rule-1"></div>
    <div class="rule rule-2"></div>
    <div class="person">
      <p class="person-name"><span class="first">Daniel</span> Whitmore</p>
      <p class="person-role">Managing Director</p>
    </div>
    <div class="rule rule-3"></div>
    <p class="address">2870 Ridgeview Lane, Westfield, 402118.</p>
    <div class="contact">
      <p><span class="label">T:</span>(044) 555 018 274 &nbsp;<span class="label">F:</span>(044) 555 018 275 &nbsp;<span class="label">M:</span>(044) 555 018 276</p>
      <p><span class="label">E:</span>info@hollowbrookhomes.com <span class="web">www.hollowbrookhomes.com</span></p>
    </div>
    <div class="follow">
      <span class="follow-label">FOLLOW US ON</span>
      <span class="social-dot"></span>
      <span class="social-dot"></span>
      <span class="social-dot"></span>
      <span class="social-dot"></span>
      <span class="social-dot alt"></span>
    </div>
  </section>

  <section class="card card-back" aria-label="Business card back">
    <div class="emboss-field" role="img" aria-label="Blind-embossed repeating brand pattern on white paper"></div>
    <div class="back-brand"><span class="brand-mark"></span>Hollowbrook</div>
  </section>
</main>
</body>
</html>
```